Website design for a construction company

The logo and the copies of all the 3 pages are attached below. I don't have a preference in colors but I would ideally like to use the colors on my logo, dark teal (secondary) and copper (primary).

Company Name: Tarnwell Group

Location: London, UK

Business Overview:

Tarnwell Group is a comprehensive construction company based in London, specializing in a wide range of construction services. We cater to various sectors, providing services including electrical work, painting and decorating, plastering, plumbing, carpentry, kitchen and bathroom installations, loft conversions, and extensions. Our team is known for its skilled craftsmanship, attention to detail, and commitment to quality.

What "TARNWELL" stands for:

Our company name, 'TARNWELL', is derived from Tarnwellion, the ancient Greek god of craftsmen, blacksmiths, artisans, sculptors, metals, metallurgy, fire, and volcanoes. Tarnwellion was renowned in mythology for his incredible skill in crafting and creating, making him the patron of all craftsmen and artisans. His name is synonymous with the mastery of artisanship and the creation of wondrous, enduring works.

In choosing 'TARNWELL' as our name, we embody the spirit and skills of Tarnwellion. It reflects our commitment to craftsmanship, excellence, and durability in the field of construction. Just as Tarnwellion was known for his meticulous work, precision, and innovative creations, our company strives to uphold these qualities in every project we undertake.

Our name is a constant reminder of our dedication to quality, innovation, and the art of building. It symbolizes our endeavor to achieve the highest standards in construction, much like Tarnwellion did in his timeless creations. In essence, 'TARNWELL' is not just our name; it's a representation of our ethos and the high standards we set for ourselves in the construction industry.

Target Audience:

Our primary audience includes homeowners, real estate developers, and commercial clients in London seeking reliable, high-quality construction services.

Unique Selling Points:

Diverse Range of Services: Offering a one-stop solution for all construction needs.

Certified and Experienced: Professional team with a strong focus on delivering certified and compliant work, particularly in electrical services.

Client-Centric Approach: Emphasizing client satisfaction, we tailor our services to meet the unique needs and visions of our clients.

Quality and Reliability: Commitment to high-quality materials, skilled workmanship, and delivering projects on time and within budget.

Website Requirements:

Clean, professional design reflecting the quality and reliability of our services.

User-friendly navigation to easily access information about our services, portfolio, company background, and contact details.

Portfolio section showcasing our past projects with placeholders for images and descriptions.

Integration of a contact form, map for our location, and links to our social media accounts.

Mobile-responsive design to ensure accessibility across various devices.

Purpose of the Website:
The website aims to:

Establish an online presence and credibility in the construction industry.

Provide an informative resource about our services and past projects to potential clients.

Facilitate easy communication and inquiries through an integrated contact system.

Tone and Style:

Professional, informative, and welcoming. The website should convey trustworthiness and expertise in the construction field.

Target Market(s)

homeowners, real estate developers, and commercial clients

Industry/Entity Type

Construction

Number of Pages Required

3 page

Colors

Designer to choose colors to be used in the design.

```html
<!DOCTYPE html>
<html lang="en">
<head>
<meta charset="UTF-8">
<title>Tarnwell Group – Construction in London</title>
<link href="https://fonts.googleapis.com/css2?family=Outfit:wght@400;500;600&family=Arimo:wght@400;700&display=swap" rel="stylesheet">
<style>
  :root {
    --copper: #B08542;
    --teal: #17918A;
    --ink: #111111;
    --paper: #FFFFFF;
  }
  * { margin: 0; padding: 0; box-sizing: border-box; }
  html, body { width: 814px; height: 1200px; overflow: hidden; background: var(--paper); }
  .page { position: relative; width: 814px; height: 1200px; font-family: "Arimo", Arial, sans-serif; color: var(--ink); }

  .brand { position: absolute; left: 142px; top: 24px; display: flex; align-items: center; gap: 5px; }
  .brand-mark { width: 12px; height: 12px; background: var(--teal); }
  .brand-name { font-family: "Outfit", sans-serif; font-weight: 400; font-size: 15px; color: var(--ink); letter-spacing: 0.4px; }

  .main-nav { position: absolute; top: 34px; left: 410px; }
  .main-nav a { position: absolute; font-family: "Outfit", sans-serif; font-size: 8px; color: var(--ink); text-decoration: none; white-space: nowrap; }

  .hero-skyline { position: absolute; left: 273px; top: 112px; width: 280px; height: 106px;
    background: linear-gradient(180deg, #fbf6ee 0%, #f1e4cf 100%); }
  .hero-title { position: absolute; top: 244px; left: 0; width: 814px; text-align: center;
    font-family: "Outfit", sans-serif; font-weight: 600; font-size: 33px; color: var(--copper); }
  .hero-subtitle { position: absolute; top: 295px; left: 0; width: 814px; text-align: center;
    font-family: "Outfit", sans-serif; font-weight: 500; font-size: 14.5px; color: var(--ink); }
  .hero-button { position: absolute; left: 365px; top: 357px; width: 97px; height: 30px; background: var(--copper);
    color: #fff; font-weight: 700; font-size: 10px; display: flex; align-items: center; justify-content: center; letter-spacing: 0.2px; }

  .welcome { position: absolute; left: 123px; top: 458px; width: 567px; height: 165px; display: flex; }
  .welcome-text { width: 217px; background: var(--teal); color: #fff; text-align: center; padding: 24px 15px 0; }
  .welcome-text h2 { font-size: 14px; font-weight: 700; margin-bottom: 12px; }
  .welcome-text p { font-size: 10px; line-height: 12.7px; hyphens: auto; -webkit-hyphens: auto; }
  .welcome-photo { flex: 1; background: linear-gradient(135deg, #a8957c 0%, #c2ac8d 45%, #8d7a64 100%); }

  .why-heading { position: absolute; left: 136px; top: 690px; font-size: 13px; font-weight: 700; }
  .why-card { position: absolute; top: 694px; width: 130px; height: 147px; color: #fff; padding: 11px 12px; }
  .why-card h3 { font-size: 10px; font-weight: 700; margin-bottom: 12px; }
  .why-card p { font-size: 7.7px; line-height: 9.9px; hyphens: auto; -webkit-hyphens: auto; }
  .card-copper { background: var(--copper); }
  .card-teal { background: var(--teal); }

  .services-intro { position: absolute; left: 132px; top: 920px; width: 550px; text-align: center;
    font-size: 13.6px; font-weight: 700; line-height: 17px; }

  .service { position: absolute; width: 80px; text-align: center; color: var(--copper); font-weight: 700; font-size: 10px; line-height: 12.6px; }
  .service svg { display: block; margin: 0 auto 7px; width: 28px; height: 28px; fill: none; stroke: var(--copper); stroke-width: 1.3; stroke-linejoin: round; stroke-linecap: round; }
</style>
</head>
<body>
<div class="page" lang="en">

  <header>
    <div class="brand"><span class="brand-mark"></span><span class="brand-name">TARNWELL</span></div>
    <nav class="main-nav">
      <a href="#" style="left:0">HOME</a>
      <a href="#" style="left:44px">ABOUT US</a>
      <a href="#" style="left:104px">SERVICES</a>
      <a href="#" style="left:161px">PROJECTS</a>
      <a href="#" style="left:221px">CONTACT US</a>
    </nav>
  </header>

  <section class="hero">
    <div class="hero-skyline" role="img" aria-label="Line illustration of the London skyline in copper"></div>
    <h1 class="hero-title">Building Your Dreams Into Reality</h1>
    <p class="hero-subtitle">Expert Craftsmanship Meets Unmatched Reliability in the Heart of London</p>
    <a class="hero-button">CONTACT US</a>
  </section>

  <section class="welcome">
    <div class="welcome-text">
      <h2>Welcome to Tarnwell Group</h2>
      <p>Where Construction Meets Excellence. Based in London, we are committed to transforming your spaces into exceptional places. Our team is dedicated to delivering the highest quality in every project, attending to every detail with precision and care.</p>
    </div>
    <div class="welcome-photo" role="img" aria-label="Overhead photo of construction workers in hard hats reviewing plans on site"></div>
  </section>

  <section class="why">
    <h2 class="why-heading">Why Choose Us</h2>
    <div class="why-card card-copper" style="left:277px">
      <h3>Our Expertise:</h3>
      <p>"Leveraging over 10 years of experience, Tarnwell Group stands as a beacon of excellence in the construction industry. We handle each project, big or small, with unmatched professionalism and skill."</p>
    </div>
    <div class="why-card card-teal" style="left:419px">
      <h3>Quality Assurance:</h3>
      <p>"Quality is not just a promise, but a practice. Meticulous attention to detail ensures flawless finishes and durable structures, bringing long-lasting satisfaction to our clients."</p>
    </div>
    <div class="why-card card-copper" style="left:561px">
      <h3>Certified Excellence:</h3>
      <p>"Your safety and satisfaction are our top priorities. We provide electrical certificates and adhere to the highest industry standards, offering peace of mind in every service."</p>
    </div>
  </section>

  <section class="services">
    <p class="services-intro">"Our Services – Tailored to Your Needs. Discover how we can bring your vision to life, covering every aspect of construction from the initial design to the final touches."</p>

    <div class="service" style="left:236px;top:1016px">
      <svg viewBox="0 0 28 28"><path d="M14 3 L26 24 H2 Z"/><path d="M15 9 L11 16 H15 L13 21 L18 13 H14 Z"/></svg>
      Electrical Work
    </div>
    <div class="service" style="left:330px;top:1016px">
      <svg viewBox="0 0 28 28"><path d="M4 18 L10 24 L16 18 L10 12 Z"/><path d="M13 15 L22 6"/><circle cx="23" cy="5" r="2"/><path d="M7 21 L12 16"/></svg>
      Painting and Decorating
    </div>
    <div class="service" style="left:424px;top:1016px">
      <svg viewBox="0 0 28 28"><path d="M3 24 Q14 12 25 24 Z"/><path d="M14 18 V5"/><rect x="12" y="2" width="4" height="4"/></svg>
      Plastering
    </div>
    <div class="service" style="left:519px;top:1016px">
      <svg viewBox="0 0 28 28"><path d="M20 3 V17 A6 6 0 0 1 8 17 V14"/><path d="M24 3 V17 A10 10 0 0 1 4 17 V14"/><rect x="2" y="9" width="8" height="5"/><rect x="18" y="1" width="8" height="3"/></svg>
      Plumbing
    </div>

    <div class="service" style="left:240px;top:1116px">
      <svg viewBox="0 0 28 28"><path d="M4 20 L18 6 L24 12 L10 26 Z"/><path d="M4 20 L2 22 L6 26 L10 26"/><circle cx="8" cy="22" r="1.5"/></svg>
      Carpentry
    </div>
    <div class="service" style="left:330px;top:1116px">
      <svg viewBox="0 0 28 28"><path d="M14 1 V8"/><path d="M9 12 H19 L14 26 Z"/><path d="M10 8 H18 V12 H10 Z"/></svg>
      Kitchen and Bathroom Installations
    </div>
    <div class="service" style="left:424px;top:1116px">
      <svg viewBox="0 0 28 28"><path d="M5 2 H10 V19 H26 V25 H5 Z"/><path d="M5 7 H8 M5 11 H8 M5 15 H8"/><circle cx="21" cy="22" r="1"/></svg>
      Loft Conversions
    </div>
    <div class="service" style="left:519px;top:1116px">
      <svg viewBox="0 0 28 28"><rect x="5" y="2" width="7" height="24"/><path d="M5 7 H8 M5 12 H8 M5 17 H8 M5 22 H8"/><path d="M17 4 H22 V20 L19.5 25 L17 20 Z"/></svg>
      Extensions
    </div>
  </section>

</div>
</body>
</html>
```